Vireo M.K. - Diagnostic Ultrasound Flyer

About US
Vireo M.K. is a concierge ultrasound company that provides onsite or offsite diagnostic ultrasounds. We have over 14 years experience in sonography, business management, and customer service. We offer both the physician and patient flexibility, convenience, and access to timely services.

We provide ultrasounds for the following specialties:
Obstetrics/Gynecology
Abdominal
Small Parts
Vascular

Company Features:
1. Onsite or Offsite Scans
2. Images Available Immediately for Referring Physician and Patient
3. Flexible Options for Ultrasound Interpretation/Billing
4. Access to Interpreting Radiologist
5. Final Report Process - 1-2 Business Days/ 1 hour for STAT.
6. PACS Storage with Secure Access.

We need a place to add in our contact information (address, email, website, phone)

We already have a logo and would like to use it ( they are attached). We would the colors to match the logo colors....maybe lighter version of yellow and blue.

```html
<!DOCTYPE html>
<html lang="en">
<head>
<meta charset="utf-8">
<title>Vireo M.K. – Diagnostic Ultrasound Flyer</title>
<link rel="stylesheet" href="https://fonts.googleapis.com/css2?family=Figtree:wght@400;500;600;700;800&display=swap">
<style>
  :root {
    --brand-blue: #1a1ea6;
    --brand-yellow: #fbbd2a;
    --ink: #222230;
    --lavender: #7d80d2;
    --paper-top: #ffffff;
    --paper-bottom: #efe9f1;
  }
  * { box-sizing: border-box; margin: 0; padding: 0; }
  html, body { width: 1004px; height: 1200px; overflow: hidden; background: #fff; }
  body { font-family: "Figtree", sans-serif; color: var(--ink); }

  .flyer {
    position: relative; width: 1004px; height: 1200px; overflow: hidden;
    background: linear-gradient(180deg, var(--paper-top) 0%, #f6f2f6 45%, var(--paper-bottom) 100%);
  }

  .brand {
    position: absolute; top: 52px; left: 0; width: 100%;
    display: flex; justify-content: center; align-items: center; gap: 16px;
  }
  .brand-dot { width: 22px; height: 22px; border-radius: 50%; background: var(--brand-yellow); }
  .brand-name { font-size: 58px; font-weight: 800; color: var(--brand-blue); letter-spacing: 3px; line-height: 1; }

  .pill {
    position: absolute; left: 50%; transform: translateX(-50%);
    border-radius: 20px; font-weight: 700; text-align: center; white-space: nowrap;
  }
  .pill-about { top: 143px; width: 188px; height: 34px; line-height: 34px; font-size: 26px; background: var(--brand-yellow); color: var(--ink); }
  .pill-features { top: 500px; width: 350px; height: 36px; line-height: 36px; font-size: 27px; background: var(--brand-blue); color: #fff; letter-spacing: .3px; }

  .about-text {
    position: absolute; top: 194px; left: 95px; width: 814px;
    text-align: center; font-size: 18px; line-height: 21.5px; color: var(--ink);
  }

  .specialties-title {
    position: absolute; top: 288px; left: 0; width: 100%; text-align: center;
    font-size: 30px; font-weight: 700; color: var(--brand-blue);
  }

  .specialty { position: absolute; top: 338px; width: 200px; margin-left: -100px; text-align: center; }
  .specialty-icon {
    display: block; width: 74px; height: 74px; margin: 0 auto 14px;
    border-radius: 50%; background: var(--brand-yellow); border: 2px solid var(--brand-blue);
  }
  .specialty-label { font-size: 27px; font-weight: 500; line-height: 32px; color: var(--ink); }

  .features { position: absolute; top: 558px; list-style: none; font-size: 17.5px; line-height: 21px; color: #2a2a36; }
  .features li { margin-bottom: 8px; }
  .features b { font-weight: 700; }
  .features-left { left: 103px; width: 330px; }
  .features-right { left: 583px; width: 330px; }

  .photo {
    position: absolute; top: 690px; left: 0; width: 1004px; height: 418px;
    background:
      radial-gradient(ellipse at 45% 45%, #5a5866 0 16%, transparent 30%),
      linear-gradient(90deg, #f3eee6 0%, #e9e3ea 40%, #e7e2ec 70%, #8fa8c8 100%);
    opacity: .95;
  }

  .contact-band { position: absolute; top: 1107px; left: 0; width: 1004px; height: 93px; }
  .contact-band svg { position: absolute; inset: 0; }
  .contact-heading {
    position: absolute; top: 1110px; left: 84px; font-size: 25px; font-weight: 700; color: var(--ink);
  }
  .contact-line {
    position: absolute; top: 1151px; left: 84px; font-size: 16px; color: var(--ink);
    display: flex; align-items: center; gap: 8px; white-space: nowrap;
  }
  .contact-line svg { width: 13px; height: 13px; }
  .contact-line .sep { color: #555; }
  .address {
    position: absolute; top: 1136px; left: 640px; display: flex; gap: 8px;
    font-size: 17px; line-height: 22px; color: #fff;
  }
  .address svg { width: 16px; height: 20px; margin-top: 2px; flex: none; }
</style>
</head>
<body>
<main class="flyer">
  <header class="brand">
    <span class="brand-dot"></span>
    <span class="brand-name">VIREO M.K.</span>
  </header>

  <div class="pill pill-about">ABOUT US</div>
  <p class="about-text">Vireo M.K. is a concierge ultrasound company that provides onsite or offsite diagnostic ultrasounds. We have over 14 years experience in sonography, business management, and customer service. We offer both the physician and patient flexibility, convenience, and access to timely services.</p>

  <h2 class="specialties-title">We provide ultrasounds for the following specialties:</h2>

  <div class="specialty" style="left:184px">
    <span class="specialty-icon" role="img" aria-label="Obstetrics and gynecology icon"></span>
    <p class="specialty-label">Obstetrics/<br>Gynecology</p>
  </div>
  <div class="specialty" style="left:414px">
    <span class="specialty-icon" role="img" aria-label="Abdominal icon"></span>
    <p class="specialty-label">Abdominal</p>
  </div>
  <div class="specialty" style="left:636px">
    <span class="specialty-icon" role="img" aria-label="Small parts icon"></span>
    <p class="specialty-label">Small Parts</p>
  </div>
  <div class="specialty" style="left:845px">
    <span class="specialty-icon" role="img" aria-label="Vascular icon"></span>
    <p class="specialty-label">Vascular</p>
  </div>

  <div class="pill pill-features">COMPANY FEATURES:</div>

  <ol class="features features-left">
    <li><b>1.</b> Onsite or Offsite Scans</li>
    <li><b>2.</b> Images Available Immediately for Referring Physician and Patient</li>
    <li><b>3.</b> Flexible Options for Ultrasound Interpretation/Billing</li>
  </ol>
  <ol class="features features-right">
    <li><b>4.</b> Access to Interpreting Radiologist</li>
    <li><b>5.</b> Final Report Process -<br>1-2 Business Days/ 1 hour for STAT.</li>
    <li><b>6.</b> PACS Storage with Secure Access.</li>
  </ol>

  <div class="photo" role="img" aria-label="Photo of a sonographer performing an ultrasound on a smiling patient while her partner watches the monitor"></div>

  <footer class="contact-band">
    <svg width="1004" height="93" viewBox="0 0 1004 93" aria-hidden="true">
      <rect x="0" y="0" width="600" height="35" fill="var(--brand-yellow)"/>
      <rect x="0" y="35" width="640" height="58" fill="#ffffff"/>
      <polygon points="571,0 1004,0 1004,93 623,93" fill="var(--lavender)"/>
    </svg>
  </footer>
  <p class="contact-heading">Contact us to make an appointment:</p>
  <p class="contact-line">
    <svg viewBox="0 0 24 24" fill="none" stroke="var(--brand-blue)" stroke-width="2"><path d="M5 3h4l2 5-3 2a12 12 0 0 0 6 6l2-3 5 2v4a2 2 0 0 1-2 2A18 18 0 0 1 3 5a2 2 0 0 1 2-2z"/></svg>
    (555) 014-2290 <span class="sep">|</span>
    <svg viewBox="0 0 24 24" fill="none" stroke="var(--brand-blue)" stroke-width="2"><circle cx="12" cy="12" r="10"/><path d="M2 12h20M12 2c3 3 3 17 0 20M12 2c-3 3-3 17 0 20"/></svg>
    www.vireo-mk.com <span class="sep">|</span>
    <svg viewBox="0 0 24 24" fill="none" stroke="var(--brand-blue)" stroke-width="2"><rect x="2" y="5" width="20" height="14"/><path d="M2 5l10 8 10-8"/></svg>
    info@vireo-mk.com
  </p>
  <address class="address" style="font-style:normal">
    <svg viewBox="0 0 16 20"><path d="M8 0a6 6 0 0 0-6 6c0 5 6 11 6 11s6-6 6-11a6 6 0 0 0-6-6z" fill="var(--brand-yellow)"/><circle cx="8" cy="6" r="2.2" fill="var(--lavender)"/><ellipse cx="8" cy="18.5" rx="5" ry="1.3" fill="none" stroke="var(--brand-yellow)"/></svg>
    <span>4810 Larkspur Park Road Suite B4<br>Fairhaven, MD 20999 USA</span>
  </address>
</main>
</body>
</html>
```